Business card for exciting VC company

Should look simple, crisp, and modern.

Industry/Entity Type

Venture Capital

Contact Information for Business Card

Would like to see at least one design that has our blue on the back with the tagline "Transforming Traditional Industry" and white front with contact details.

Font styles to use
Sans Serif

Requirements
Must have
• Logo

Darius Pellworth
dpellworth@brindlegate.vc
Managing Partner
M (628)304-xxxx

```html
<!DOCTYPE html>
<html lang="en">
<head>
<meta charset="utf-8">
<title>Brindlegate Capital – Business Cards</title>
<link href="https://fonts.googleapis.com/css2?family=Montserrat:wght@400;500;600&display=swap" rel="stylesheet">
<style>
  :root {
    --stage: #151515;
    --card: #262626;
    --card-deep: #1d1d1d;
    --map-tone: #303030;
    --brand-blue: #3f82d4;
    --ink-light: #f2f2f2;
    --ink-muted: #8c8c8c;
  }
  * { box-sizing: border-box; margin: 0; padding: 0; }
  html, body {
    width: 1200px; height: 900px; overflow: hidden;
    background: var(--stage);
    font-family: "Montserrat", sans-serif;
  }
  .stage {
    width: 1200px; height: 900px;
    display: flex; flex-direction: column; align-items: center; justify-content: center;
    gap: 40px;
  }
  .card {
    position: relative;
    width: 760px; height: 400px;
    background: linear-gradient(135deg, var(--card) 0%, var(--card-deep) 100%);
    border-bottom: 6px solid var(--brand-blue);
    overflow: hidden;
    box-shadow: 0 18px 40px rgba(0,0,0,.55);
  }
  .world-map {
    position: absolute; left: 40px; top: 30px; width: 680px; height: 330px;
    border-radius: 40px;
    background: radial-gradient(ellipse at 50% 45%, var(--map-tone) 0%, rgba(48,48,48,.35) 55%, rgba(38,38,38,0) 80%);
  }
  /* Back */
  .card--back .wordmark {
    position: absolute; left: 0; right: 0; top: 150px;
    text-align: center;
    font-size: 54px; font-weight: 500; letter-spacing: 6px;
    color: var(--ink-muted);
  }
  /* Front */
  .card--front .wordmark {
    position: absolute; left: 36px; top: 34px;
    font-size: 28px; font-weight: 500; letter-spacing: 4px;
    color: var(--ink-light);
  }
  .divider {
    position: absolute; left: 70px; right: 60px; top: 250px;
    height: 2px; background: var(--brand-blue);
  }
  .identity {
    position: absolute; right: 60px; top: 178px; text-align: right;
  }
  .identity .name {
    font-size: 21px; font-weight: 500; letter-spacing: 1.5px;
    color: var(--brand-blue); text-transform: uppercase;
  }
  .identity .role {
    margin-top: 4px; font-size: 18px; color: var(--ink-light); letter-spacing: .5px;
  }
  .contact {
    position: absolute; right: 40px; top: 272px; list-style: none; text-align: right;
  }
  .contact li {
    display: flex; align-items: center; justify-content: flex-end; gap: 10px;
    font-size: 19px; color: var(--ink-light); line-height: 32px;
  }
  .contact svg { width: 16px; height: 16px; flex: none; }
</style>
</head>
<body>
<main class="stage">
  <section class="card card--back">
    <div class="world-map" role="img" aria-label="Faint world map background"></div>
    <div class="wordmark">BRINDLEGATE CAPITAL</div>
  </section>

  <section class="card card--front">
    <div class="world-map" role="img" aria-label="Faint world map background"></div>
    <div class="wordmark">BRINDLEGATE CAPITAL</div>
    <div class="identity">
      <p class="name">Darius Pellworth</p>
      <p class="role">Managing Partner</p>
    </div>
    <div class="divider"></div>
    <ul class="contact">
      <li>(628)304-xxxx
        <svg viewBox="0 0 16 16" aria-hidden="true"><path d="M4 1.5 L6 4.5 L4.8 6 C5.6 8 7.8 10.4 10 11.2 L11.5 10 L14.5 12 L13 14.5 C7 14 2 9 1.5 3 Z" fill="none" stroke="var(--brand-blue)" stroke-width="1.5" stroke-linejoin="round"/></svg>
      </li>
      <li>dpellworth@brindlegate.vc
        <svg viewBox="0 0 16 16" aria-hidden="true"><rect x="1.5" y="3.5" width="13" height="9" fill="none" stroke="var(--brand-blue)" stroke-width="1.5"/><path d="M1.5 3.5 L8 9 L14.5 3.5" fill="none" stroke="var(--brand-blue)" stroke-width="1.5"/></svg>
      </li>
    </ul>
  </section>
</main>
</body>
</html>
```